Folded A4 flyer for design&construction company

Folded A4 flyer needed. Keywords: elegant, stylish
our website www.corvimo.ae

Industry/Entity Type

Construction

```html
<!DOCTYPE html>
<html lang="en">
<head>
<meta charset="utf-8">
<title>Corvimo – Folded Flyer</title>
<link href="https://fonts.googleapis.com/css2?family=Barlow+Semi+Condensed:wght@300;400;500&family=Cormorant+Garamond:ital,wght@1,500&display=swap" rel="stylesheet">
<style>
  :root{
    --gold:#b8995c;
    --tan:#b49a6c;
    --ink:#1e1c1a;
    --dark:#1f1d1b;
    --paper:#ffffff;
    --text:#2a2826;
  }
  *{box-sizing:border-box;margin:0;padding:0}
  html,body{width:1200px;height:1200px;overflow:hidden;background:#fff}
  body{position:relative;font-family:"Barlow Semi Condensed",sans-serif;color:var(--text)}
  .page{position:absolute;overflow:hidden}
  .photo{position:absolute}

  /* top spread: back page */
  .back{left:208px;top:46px;width:390px;height:542px;background:var(--paper)}
  .back .photo{left:0;top:0;width:390px;height:268px;
    background:linear-gradient(135deg,#d9d4cc 0%,#8c8478 35%,#3d3833 70%,#6b5a3e 100%)}
  .about{position:absolute;left:58px;top:294px;width:274px;font-size:7.2px;line-height:10.4px;text-align:center;font-weight:400}
  .quote-call{position:absolute;left:0;width:390px;top:378px;text-align:center}
  .quote-call h2{font-weight:400;font-size:13.5px;color:var(--gold);letter-spacing:.2px}
  .quote-call p{font-size:10px;line-height:13.5px}
  .web{position:absolute;top:461px;left:0;width:390px;text-align:center}
  .web span{display:inline-block;background:var(--ink);color:#fff;font-size:10.5px;padding:1px 4px}
  .address{position:absolute;top:481px;left:57px;width:278px;text-align:center;font-size:10px;padding-bottom:3px;border-bottom:1px solid var(--ink)}

  /* top spread: cover */
  .cover{left:598px;top:46px;width:388px;height:542px;background:var(--dark)}
  .cover svg{position:absolute;left:0;top:0}
  .cover-badge{position:absolute;left:96px;top:193px;width:192px;height:192px;border-radius:50%;
    background:radial-gradient(circle,#fff 60%,#f3ead8 100%);border:3px solid var(--gold);
    display:flex;flex-direction:column;align-items:center;justify-content:center}
  .cover-badge .name{font-size:46px;font-weight:400;color:var(--ink);letter-spacing:1px;line-height:1}
  .cover-badge .tag{font-size:11px;font-weight:400;color:var(--ink);margin-top:4px}
  .motto{position:absolute;left:0;width:388px;top:440px;text-align:center;color:var(--gold);font-weight:300;font-size:9px;line-height:15px}

  /* bottom spread: service panels */
  .panel{width:390px}
  .p-design{left:208px;top:611px;height:281px}
  .p-fitout{left:598px;top:611px;width:387px;height:281px}
  .p-land{left:208px;top:892px;height:260px}
  .p-maint{left:598px;top:892px;width:387px;height:260px}
  .panel .photo{inset:0}
  .p-design .photo{background:linear-gradient(160deg,#efe1c6 0%,#c9a97a 45%,#8a5d34 100%)}
  .p-fitout .photo{background:linear-gradient(135deg,#2b2722 0%,#5a5045 45%,#e6e3de 75%,#2a2723 100%)}
  .p-land .photo{background:linear-gradient(120deg,#6b4a25 0%,#b08a55 40%,#e8cf95 60%,#7d5a31 100%)}
  .p-maint .photo{background:linear-gradient(150deg,#294a73 0%,#5d89b8 40%,#2a3f66 75%,#5a3a2f 100%)}

  .card{position:absolute;background:#fff;border-radius:0 0 4px 4px}
  .card-head{height:18px;background:var(--tan);color:#fff;font-size:10px;line-height:18px;padding-left:8px;letter-spacing:.3px;position:relative}
  .card-badge{position:absolute;right:6px;top:-17px;width:52px;height:52px;border-radius:50%;background:#fff;
    display:flex;align-items:center;justify-content:center;font-size:12.5px;color:var(--ink);letter-spacing:.3px}
  .card ul{list-style:none;padding:10px 8px 8px 8px}
  .card li{font-size:10px;line-height:13.3px;padding-left:16px;position:relative;color:var(--text)}
  .card li svg{position:absolute;left:2px;top:3px}

  .p-design .card{left:36px;top:51px;width:158px}
  .p-fitout .card{left:204px;top:51px;width:157px}
  .p-land .card{left:215px;top:82px;width:135px}
  .p-maint .card{left:35px;top:52px;width:130px}
</style>
</head>
<body>

<!-- Top spread: back page -->
<section class="page back">
  <div class="photo" role="img" aria-label="Photo of a modern dining room and kitchen with chandeliers"></div>
  <p class="about">We believe in quality beginnings and flawless finishes. We are a team of creative designers and constructors with years of experience and expertise in providing complete interior design and construction services. Our unique designing prowess is complemented by our unflinching commitment to quality construction. Our team specializes in classic and contemporary high quality construction in Dubai for commercial and residential projects.</p>
  <div class="quote-call">
    <h2>GET A FREE QUOTE TODAY!</h2>
    <p>800 – CORVIMO<br>OR<br>CONTACT@CORVIMO.AE</p>
  </div>
  <div class="web"><span>www.corvimo.ae</span></div>
  <p class="address">Corvimo LLC, Harbor Gate Tower, Office 904, Marina Quarter, Dubai</p>
</section>

<!-- Top spread: cover -->
<section class="page cover">
  <svg width="388" height="542" viewBox="0 0 388 542" role="img" aria-label="Photo of a bright interior with an orange curved ceiling and spiral staircase">
    <defs>
      <linearGradient id="coverPhoto" x1="0" y1="0" x2="1" y2="1">
        <stop offset="0" stop-color="#f2efe9"/>
        <stop offset=".45" stop-color="#e9a83a"/>
        <stop offset="1" stop-color="#b9782d"/>
      </linearGradient>
    </defs>
    <rect width="388" height="300" fill="url(#coverPhoto)"/>
    <path d="M0,282 C110,282 170,246 388,246 L388,542 L0,542 Z" fill="#1f1d1b"/>
  </svg>
  <div class="cover-badge">
    <span class="name">CORVIMO</span>
    <span class="tag">design &amp; construction</span>
  </div>
  <p class="motto">Quality is not an act, it is a habit<br>Theon Valaris</p>
</section>

<!-- Bottom spread: design -->
<section class="page panel p-design">
  <div class="photo" role="img" aria-label="Photo of a warm classic living room with armchairs and chandelier"></div>
  <div class="card">
    <div class="card-head">DESIGN<span class="card-badge">CORVIMO</span></div>
    <ul>
      <li><svg width="8" height="7" viewBox="0 0 8 7"><path d="M1 1l3 2.5L1 6M4 1l3 2.5L4 6" fill="none" stroke="#b8995c" stroke-width="1"/></svg>Villas Interior Design</li>
      <li><svg width="8" height="7" viewBox="0 0 8 7"><path d="M1 1l3 2.5L1 6M4 1l3 2.5L4 6" fill="none" stroke="#b8995c" stroke-width="1"/></svg>Villas Exterior Design</li>
      <li><svg width="8" height="7" viewBox="0 0 8 7"><path d="M1 1l3 2.5L1 6M4 1l3 2.5L4 6" fill="none" stroke="#b8995c" stroke-width="1"/></svg>Landscape Design</li>
      <li><svg width="8" height="7" viewBox="0 0 8 7"><path d="M1 1l3 2.5L1 6M4 1l3 2.5L4 6" fill="none" stroke="#b8995c" stroke-width="1"/></svg>Retail Interior Design</li>
      <li><svg width="8" height="7" viewBox="0 0 8 7"><path d="M1 1l3 2.5L1 6M4 1l3 2.5L4 6" fill="none" stroke="#b8995c" stroke-width="1"/></svg>Office Interior Design</li>
      <li><svg width="8" height="7" viewBox="0 0 8 7"><path d="M1 1l3 2.5L1 6M4 1l3 2.5L4 6" fill="none" stroke="#b8995c" stroke-width="1"/></svg>Hospitality Interior Design</li>
      <li><svg width="8" height="7" viewBox="0 0 8 7"><path d="M1 1l3 2.5L1 6M4 1l3 2.5L4 6" fill="none" stroke="#b8995c" stroke-width="1"/></svg>Hotel Interior Design</li>
      <li><svg width="8" height="7" viewBox="0 0 8 7"><path d="M1 1l3 2.5L1 6M4 1l3 2.5L4 6" fill="none" stroke="#b8995c" stroke-width="1"/></svg>Hotel Exterior Design</li>
      <li><svg width="8" height="7" viewBox="0 0 8 7"><path d="M1 1l3 2.5L1 6M4 1l3 2.5L4 6" fill="none" stroke="#b8995c" stroke-width="1"/></svg>Restaurant Interior Design</li>
    </ul>
  </div>
</section>

<!-- Bottom spread: fitout -->
<section class="page panel p-fitout">
  <div class="photo" role="img" aria-label="Photo of a dark tiled bathroom with a freestanding bathtub and chandelier"></div>
  <div class="card">
    <div class="card-head">FITOUT<span class="card-badge">CORVIMO</span></div>
    <ul>
      <li><svg width="8" height="7" viewBox="0 0 8 7"><path d="M1 1l3 2.5L1 6M4 1l3 2.5L4 6" fill="none" stroke="#b8995c" stroke-width="1"/></svg>Development Approvals</li>
      <li><svg width="8" height="7" viewBox="0 0 8 7"><path d="M1 1l3 2.5L1 6M4 1l3 2.5L4 6" fill="none" stroke="#b8995c" stroke-width="1"/></svg>Flooring Solutions</li>
      <li><svg width="8" height="7" viewBox="0 0 8 7"><path d="M1 1l3 2.5L1 6M4 1l3 2.5L4 6" fill="none" stroke="#b8995c" stroke-width="1"/></svg>Partition</li>
      <li><svg width="8" height="7" viewBox="0 0 8 7"><path d="M1 1l3 2.5L1 6M4 1l3 2.5L4 6" fill="none" stroke="#b8995c" stroke-width="1"/></svg>Sealing Solutions</li>
      <li><svg width="8" height="7" viewBox="0 0 8 7"><path d="M1 1l3 2.5L1 6M4 1l3 2.5L4 6" fill="none" stroke="#b8995c" stroke-width="1"/></svg>MEP Works</li>
      <li><svg width="8" height="7" viewBox="0 0 8 7"><path d="M1 1l3 2.5L1 6M4 1l3 2.5L4 6" fill="none" stroke="#b8995c" stroke-width="1"/></svg>Civil Works</li>
      <li><svg width="8" height="7" viewBox="0 0 8 7"><path d="M1 1l3 2.5L1 6M4 1l3 2.5L4 6" fill="none" stroke="#b8995c" stroke-width="1"/></svg>Joinery</li>
      <li><svg width="8" height="7" viewBox="0 0 8 7"><path d="M1 1l3 2.5L1 6M4 1l3 2.5L4 6" fill="none" stroke="#b8995c" stroke-width="1"/></svg>Glass and Aluminium Works (subcontractor)</li>
    </ul>
  </div>
</section>

<!-- Bottom spread: landscaping -->
<section class="page panel p-land">
  <div class="photo" role="img" aria-label="Photo of a curved wooden interior with hanging globe lights and vases"></div>
  <div class="card">
    <div class="card-head">LANDSCAPING<span class="card-badge">CORVIMO</span></div>
    <ul>
      <li><svg width="8" height="7" viewBox="0 0 8 7"><path d="M1 1l3 2.5L1 6M4 1l3 2.5L4 6" fill="none" stroke="#b8995c" stroke-width="1"/></svg>Soft Landscaping</li>
      <li><svg width="8" height="7" viewBox="0 0 8 7"><path d="M1 1l3 2.5L1 6M4 1l3 2.5L4 6" fill="none" stroke="#b8995c" stroke-width="1"/></svg>Irrigation Solutions</li>
      <li><svg width="8" height="7" viewBox="0 0 8 7"><path d="M1 1l3 2.5L1 6M4 1l3 2.5L4 6" fill="none" stroke="#b8995c" stroke-width="1"/></svg>Hard land Scaping</li>
      <li><svg width="8" height="7" viewBox="0 0 8 7"><path d="M1 1l3 2.5L1 6M4 1l3 2.5L4 6" fill="none" stroke="#b8995c" stroke-width="1"/></svg>External Lighting</li>
      <li><svg width="8" height="7" viewBox="0 0 8 7"><path d="M1 1l3 2.5L1 6M4 1l3 2.5L4 6" fill="none" stroke="#b8995c" stroke-width="1"/></svg>Swimming Pool &amp; Water Features</li>
    </ul>
  </div>
</section>

<!-- Bottom spread: maintenance -->
<section class="page panel p-maint">
  <div class="photo" role="img" aria-label="Photo of a blue-lit lounge bar with a large dome pendant and leather seating"></div>
  <div class="card">
    <div class="card-head">MAINTAINCE<span class="card-badge">CORVIMO</span></div>
    <ul>
      <li><svg width="8" height="7" viewBox="0 0 8 7"><path d="M1 1l3 2.5L1 6M4 1l3 2.5L4 6" fill="none" stroke="#b8995c" stroke-width="1"/></svg>AC Repair</li>
      <li><svg width="8" height="7" viewBox="0 0 8 7"><path d="M1 1l3 2.5L1 6M4 1l3 2.5L4 6" fill="none" stroke="#b8995c" stroke-width="1"/></svg>Plumber Services</li>
      <li><svg width="8" height="7" viewBox="0 0 8 7"><path d="M1 1l3 2.5L1 6M4 1l3 2.5L4 6" fill="none" stroke="#b8995c" stroke-width="1"/></svg>Electric Repair</li>
      <li><svg width="8" height="7" viewBox="0 0 8 7"><path d="M1 1l3 2.5L1 6M4 1l3 2.5L4 6" fill="none" stroke="#b8995c" stroke-width="1"/></svg>Carpentry Work</li>
      <li><svg width="8" height="7" viewBox="0 0 8 7"><path d="M1 1l3 2.5L1 6M4 1l3 2.5L4 6" fill="none" stroke="#b8995c" stroke-width="1"/></svg>Gypsum Ceiling</li>
      <li><svg width="8" height="7" viewBox="0 0 8 7"><path d="M1 1l3 2.5L1 6M4 1l3 2.5L4 6" fill="none" stroke="#b8995c" stroke-width="1"/></svg>Painting Services</li>
      <li><svg width="8" height="7" viewBox="0 0 8 7"><path d="M1 1l3 2.5L1 6M4 1l3 2.5L4 6" fill="none" stroke="#b8995c" stroke-width="1"/></svg>Cleaning Services</li>
      <li><svg width="8" height="7" viewBox="0 0 8 7"><path d="M1 1l3 2.5L1 6M4 1l3 2.5L4 6" fill="none" stroke="#b8995c" stroke-width="1"/></svg>Emergency Services</li>
    </ul>
  </div>
</section>

</body>
</html>
```